the ridgewell craft premier branch

design a DL A4 tri fold brochure to reflect our creative landscape business
my web site www.theridgewellcraft.com.au
has all the information needed
i will also be updating the website to be more updated and creative design

```html
<!DOCTYPE html>
<html lang="en">
<head>
<meta charset="utf-8">
<title>The Ridgewell Craft – Tri-fold Brochure</title>
<link rel="stylesheet" href="https://fonts.googleapis.com/css2?family=Montserrat:wght@600;700&family=Questrial&display=swap">
<style>
:root{
  --orange:#f0901e;
  --orange-dark:#e0801a;
  --ink:#2b2b2b;
  --body:#4a4a4a;
  --blue:#2a8fd8;
  --paper:#ffffff;
  --mist:#eeeeee;
  --stage:#f2f2f2;
  --head:'Montserrat',sans-serif;
  --text:'Questrial',sans-serif;
}
*{box-sizing:border-box;margin:0;padding:0}
html,body{width:1200px;height:1000px;overflow:hidden;background:var(--stage)}
body{position:relative;font-family:var(--text);color:var(--body)}
.sheet{position:absolute;left:267px;width:665px;height:470px;display:grid;grid-template-columns:repeat(3,1fr);background:var(--paper);box-shadow:0 4px 16px rgba(0,0,0,.15)}
.sheet--inside{top:12px}
.sheet--outside{top:506px}
.panel{position:relative;overflow:hidden;border-right:1px solid #e4e4e4}
.panel:last-child{border-right:0}
.heading{font-family:var(--head);font-weight:700;font-size:13px;color:var(--ink);letter-spacing:.3px}
.heading::after{content:"";display:block;width:30px;height:1.5px;background:var(--blue);margin-top:4px}
.heading--light{color:#fff}
.heading--light::after{background:#fff}
.copy{font-size:7.6px;line-height:1.45}
.photo{border-radius:3px}

/* inside: process */
.process{padding:22px 18px}
.process .copy{margin-top:12px}
.step{display:flex;gap:8px;align-items:flex-start;margin-top:12px}
.step svg{flex:0 0 18px;margin-top:4px}
.process .cta{margin-top:16px;font-family:var(--head);font-weight:700;font-size:7.6px;color:var(--ink)}

/* inside: services & projects */
.services-block{height:270px;background:var(--orange);padding:22px 16px}
.services-block .copy{color:#fff;margin-top:9px}
.projects-block{background:var(--mist);height:200px;padding:14px 14px}
.project{display:flex;gap:8px;align-items:center;margin-top:9px}
.project .photo{width:110px;height:62px;flex:0 0 110px}
.project-name{font-family:var(--head);font-weight:700;font-size:7.6px;color:var(--ink);border-left:1px solid #bbb;padding-left:5px}
.project-name small{display:block;font-family:var(--text);font-weight:400;font-size:6.6px;color:var(--body);margin-top:2px}
.service-grid{height:270px;background:var(--orange);padding:18px 14px;display:grid;grid-template-columns:1fr 1fr;gap:8px 10px}
.service{display:flex;flex-direction:column;align-items:center;gap:5px}
.service .photo{width:100%;height:68px}
.service span{font-family:var(--head);font-weight:700;font-size:7.6px;color:#fff;text-align:center;line-height:1.2}
.projects-right{background:var(--mist);height:186px;padding:10px 14px}
.projects-right .photo{width:104px;height:76px;flex:0 0 104px}
.band{position:absolute;left:0;right:0;bottom:0;height:14px;background:var(--orange)}

/* outside: about */
.about{padding:22px 16px}
.about .copy{margin-top:9px}
.about strong{color:var(--ink)}
.about-photo{position:absolute;left:0;right:0;bottom:0;height:170px;background:linear-gradient(180deg,rgba(255,255,255,1) 0%,rgba(160,180,140,.55) 35%,#7a9a5a 100%)}

/* outside: contact */
.contact{padding:24px 16px;text-align:center}
.contact .heading{display:inline-block}
.contact .heading::after{margin:4px auto 0}
.contact-name{font-family:var(--head);font-weight:600;font-size:8px;color:var(--ink);margin-top:14px;line-height:1.4}
.contact-item{margin-top:20px;font-size:8px;color:var(--ink)}
.contact-item svg{display:block;margin:0 auto 4px}
.social{margin-top:20px;font-family:var(--head);font-weight:700;font-size:8px;color:var(--ink)}
.social-dots{display:flex;justify-content:center;gap:5px;margin:5px 0 4px}
.social-dots i{width:7px;height:7px;border-radius:50%;background:var(--blue)}
.brand{display:flex;flex-direction:column;align-items:center;gap:5px;font-family:var(--head);font-weight:700;color:var(--ink)}
.contact .brand{position:absolute;left:0;right:0;bottom:26px;font-size:10px}
.brand-dot{width:18px;height:18px;border-radius:50%;background:var(--orange)}

/* outside: cover */
.cover{display:grid;grid-template-columns:26px 1fr 1fr;grid-template-rows:repeat(5,1fr)}
.cover-strip{grid-row:1/6;background:var(--orange)}
.cover-title{background:var(--orange);color:#fff;font-family:var(--text);font-size:13px;line-height:1.2;padding:10px 6px;border:1px solid #fff}
.cover .photo{border-radius:0;border:1px solid #fff}
.cover .brand{font-size:8.5px;justify-content:center;text-align:center;padding:4px;border:1px solid #fff}
</style>
</head>
<body>

<section class="sheet sheet--inside">
  <div class="panel process">
    <h2 class="heading">THE PROCESS</h2>
    <p class="copy">TRC can work with an existing design or create a landscape design to suit your needs.</p>
    <div class="step">
      <svg width="18" height="18" viewBox="0 0 18 18"><path d="M3 3h12a2 2 0 0 1 2 2v6a2 2 0 0 1-2 2H8l-4 3v-3H3a2 2 0 0 1-2-2V5a2 2 0 0 1 2-2z" fill="var(--blue)"/><circle cx="6" cy="8" r="1" fill="#fff"/><circle cx="9" cy="8" r="1" fill="#fff"/><circle cx="12" cy="8" r="1" fill="#fff"/></svg>
      <p class="copy">Once a design has been established, Owen Hartley will go over your plans onsite and discuss the requirements to suit your space and climate and provide advice as needed.</p>
    </div>
    <div class="step">
      <svg width="18" height="18" viewBox="0 0 18 18"><rect x="2" y="1" width="14" height="16" rx="2" fill="var(--blue)"/><path d="M5 6h1M8 6h5M5 9h1M8 9h5M5 12h1M8 12h5" stroke="#fff" stroke-width="1.3"/></svg>
      <p class="copy">This is followed by a detailed quote which Owen invests his time to break down the construction elements and ensure a quality outcome for each stage.</p>
    </div>
    <div class="step">
      <svg width="18" height="18" viewBox="0 0 18 18"><circle cx="9" cy="6" r="3" fill="var(--blue)"/><circle cx="3" cy="14" r="2" fill="var(--blue)"/><circle cx="15" cy="14" r="2" fill="var(--blue)"/><path d="M9 9v3M3 12l6-1 6 1" stroke="var(--blue)" stroke-width="1.3" fill="none"/></svg>
      <p class="copy">Owen will project-manage your entire outdoor construction and ensure you are updated throughout the journey.</p>
    </div>
    <p class="copy">Our clients will experience honesty, integrity, and professionalism throughout the project which allows them to embrace their outdoor living after completion.</p>
    <p class="copy"><em>The Ridgewell Craft is a full-service landscaping and construction team that relish the journey to deliver high-end and bespoke outdoor designs.</em></p>
    <p class="cta">FOR MORE INFORMATION VISIT OUR WEBSITE.</p>
  </div>

  <div class="panel">
    <div class="services-block">
      <h2 class="heading heading--light">OUR SERVICES</h2>
      <p class="copy">As a full service landscape and construction business, we can ensure our client's outdoor vision comes to fruition from concept to completion.</p>
      <p class="copy">The Ridgewell Craft proudly offers high-end landscaping in residential and acreage environments. With extensive knowledge and experience in garden landscapes and construction, our team have the ability to work with various materials and land settings in Melbourne and surrounds.</p>
      <p class="copy">Our project management includes advice and progressive updates and we can implement large-scale projects in increments if required.</p>
    </div>
    <div class="projects-block">
      <h2 class="heading">OUR PROJECTS</h2>
      <div class="project">
        <div class="photo" role="img" aria-label="Garden path with rose archway leading to a red door" style="background:linear-gradient(135deg,#5f7a45,#b84a4a 60%,#8a8a8a)"></div>
        <p class="project-name">Williamstown Project<small>Strong and Soft Accents</small></p>
      </div>
      <div class="project">
        <div class="photo" role="img" aria-label="Lawn garden with hanging nest swing and hedges" style="background:linear-gradient(160deg,#d9d9d9,#5e7e3e 55%,#7aa048)"></div>
        <p class="project-name">Essendon Project<small>Calm and Modern</small></p>
      </div>
    </div>
  </div>

  <div class="panel">
    <div class="service-grid">
      <div class="service"><div class="photo" role="img" aria-label="3D garden design render" style="background:linear-gradient(135deg,#cfd6cc,#8ba07a)"></div><span>Consultation<br>and Design</span></div>
      <div class="service"><div class="photo" role="img" aria-label="Excavated site being prepared" style="background:linear-gradient(160deg,#b7c4cc,#7a5b40)"></div><span>Earthwork and<br>Site Preparation</span></div>
      <div class="service"><div class="photo" role="img" aria-label="Newly built garden with rendered wall" style="background:linear-gradient(160deg,#e5e5e0,#4f7a3a)"></div><span>Installation and<br>Construction</span></div>
      <div class="service"><div class="photo" role="img" aria-label="Maintained lawn and garden beds" style="background:linear-gradient(160deg,#6d8450,#3f5a2c)"></div><span>Maintenance<br>Programs</span></div>
    </div>
    <div class="projects-right">
      <div class="project">
        <div class="photo" role="img" aria-label="Modern home with structured front garden at dusk" style="background:linear-gradient(160deg,#9aa4aa,#5a6a48 60%,#3a4430)"></div>
        <p class="project-name">Toorak Landscaping<small>Refined &amp; Structured</small></p>
      </div>
      <div class="project">
        <div class="photo" role="img" aria-label="Timber deck and fenced backyard garden" style="background:linear-gradient(160deg,#8c7a66,#a06a3a 55%,#6a4a2a)"></div>
        <p class="project-name">Sunbury Landscaping<small>Easy to enjoy<br>low maintenance</small></p>
      </div>
    </div>
    <div class="band"></div>
  </div>
</section>

<section class="sheet sheet--outside">
  <div class="panel about">
    <h2 class="heading">ABOUT US</h2>
    <p class="copy"><strong>The Ridgewell Craft (TRC)</strong>, formerly Owen Hartley Landscapes, is a professional landscaping and construction service that takes pride in delivering high-end outdoor landscapes across Melbourne, Victoria.</p>
    <p class="copy">Owen Hartley, head of The Ridgewell Craft, offers a team that dedicates their efforts from concept development to installation and maintenance to ensure the outdoor creation becomes part of the client's home and life experience with visual, tactile and sensory inclusions.</p>
    <p class="copy">Over its 20 years, the business has developed a strong reputation for positive customer experiences, innovative designs and quality outcomes to suit individual needs and design styles. When working with Owen Hartley's team, you work with a qualified ensemble of experienced landscapers and horticulturalists.</p>
    <div class="about-photo" role="img" aria-label="Child on a nest swing in a green backyard lawn"></div>
  </div>

  <div class="panel contact">
    <h2 class="heading">CONTACT US</h2>
    <p class="contact-name">Owen Hartley<br>The Ridgewell Craft - Premier Branch</p>
    <div class="contact-item">
      <svg width="10" height="10" viewBox="0 0 10 10"><path d="M2 1l2 2-1 1.5c.6 1.2 1.3 1.9 2.5 2.5L7 6l2 2-1.5 1.5C4.5 9 1 5.5.5 2.5z" fill="var(--blue)"/></svg>
      0400 318 726
    </div>
    <div class="contact-item">
      <svg width="12" height="9" viewBox="0 0 12 9"><rect width="12" height="9" rx="1" fill="var(--blue)"/><path d="M0.5 0.8l5.5 4.2 5.5-4.2" stroke="#fff" fill="none"/></svg>
      info@theridgewellcraft.com.au
    </div>
    <div class="contact-item">
      <svg width="11" height="11" viewBox="0 0 11 11"><circle cx="5.5" cy="5.5" r="5" fill="var(--blue)"/><path d="M.5 5.5h10M5.5.5c-2.5 3-2.5 7 0 10M5.5.5c2.5 3 2.5 7 0 10" stroke="#fff" stroke-width=".7" fill="none"/></svg>
      www.theridgewellcraft.com.au
    </div>
    <div class="contact-item">
      <svg width="9" height="12" viewBox="0 0 9 12"><path d="M4.5 0A4.5 4.5 0 0 0 0 4.5C0 8 4.5 12 4.5 12S9 8 9 4.5A4.5 4.5 0 0 0 4.5 0z" fill="var(--blue)"/><circle cx="4.5" cy="4.5" r="1.6" fill="#fff"/></svg>
      PO BOX 742<br>Kestrel Bay VIC 3990
    </div>
    <p class="social">Follow us on Social Media</p>
    <div class="social-dots"><i></i><i></i></div>
    <p class="copy">The Ridgewell Craft Premier Branch</p>
    <div class="brand"><span class="brand-dot"></span>The Ridgewell Craft Premier Branch</div>
  </div>

  <div class="panel cover">
    <div class="cover-strip"></div>
    <div class="cover-title">Creative Landscape Design and Construction</div>
    <div class="photo" role="img" aria-label="Luxury home with blue pool at dusk" style="background:linear-gradient(180deg,#c9b08a,#3a7fb8)"></div>
    <div class="photo" role="img" aria-label="Timber pergola at sunset" style="background:linear-gradient(160deg,#d8c09a,#9a6a3a)"></div>
    <div class="photo" role="img" aria-label="Outdoor lounge with white seating" style="background:linear-gradient(160deg,#7a8a6a,#a8a8a0)"></div>
    <div class="photo" role="img" aria-label="Lit garden with tropical planting at night" style="background:linear-gradient(160deg,#3a3a2a,#5a6a3a)"></div>
    <div class="photo" role="img" aria-label="Built-in bench with orange cushions" style="background:linear-gradient(160deg,#c8b89a,#e07a40)"></div>
    <div class="photo" role="img" aria-label="Period home front garden" style="background:linear-gradient(160deg,#b89a70,#6a5a3a)"></div>
    <div class="photo" role="img" aria-label="Timber post screen with pebbles" style="background:linear-gradient(160deg,#6a6a70,#8a5a3a)"></div>
    <div class="photo" role="img" aria-label="Potted plant on timber deck" style="background:linear-gradient(180deg,#dedede,#a0582a)"></div>
    <div class="brand"><span class="brand-dot"></span>The Ridgewell Craft Premier Branch</div>
  </div>
</section>

</body>
</html>
```